Tradelo Size Charts - 6 Products

Hi Koby,

I had you in mind for this, but we have a new e-commerce store that requires the attached 6 size charts re-designed. They are terrible charts from drop shippers and we need them re-designed to match the Talvoro brand logo to designed.

Chart needs to be white background and black letter's. You can add some smart gradients or design to it if you want to make it look elegant and confident.

Can you design 1 chart and we can amend it to perfection with feedback?
Once we agree on the style - you can then do the same style and design for the remaining charts.

Let me know if this is ok?

```html
<!DOCTYPE html>
<html lang="en">
<head>
<meta charset="utf-8">
<title>Talvoro Size Detail Chart</title>
<link href="https://fonts.googleapis.com/css2?family=Source+Sans+3:wght@400;600;700&display=swap" rel="stylesheet">
<style>
  :root {
    --canvas-bg: #eceef1;
    --card-bg: #ffffff;
    --header-top: #5a5a5a;
    --header-bottom: #333333;
    --ribbon-top: #e0504f;
    --ribbon-bottom: #c94445;
    --button-red: #d9474a;
    --button-edge: #b8393b;
    --ink: #1c1c1c;
    --rule: #4a4a4a;
    --white: #ffffff;
  }
  * { margin: 0; padding: 0; box-sizing: border-box; }
  html, body {
    width: 1200px; height: 1200px; overflow: hidden;
    background: var(--canvas-bg);
    font-family: "Source Sans 3", "Myriad Pro", sans-serif;
  }
  .chart-card {
    position: absolute; left: 28px; top: 216px;
    width: 1144px; height: 767px;
    background: var(--card-bg);
  }
  .chart-panel {
    position: absolute; left: 133px; top: 44px;
    width: 878px; height: 648px;
  }
  .column {
    position: absolute; top: 60px; width: 278px; height: 588px;
    border: 1.5px solid var(--rule); border-radius: 3px;
    background: var(--card-bg);
  }
  .column--size { left: 0; }
  .column--bust { left: 299px; }
  .column--length { left: 600px; }
  .ribbon { position: absolute; left: 0; top: 0; width: 878px; height: 250px; }
  .chart-header {
    position: absolute; left: 0; top: 0; width: 878px; height: 70px;
    background: linear-gradient(var(--header-top), var(--header-bottom));
    border-radius: 4px 4px 0 0;
    color: var(--white); font-weight: 700; font-size: 21px;
    display: flex; align-items: center; justify-content: center;
    letter-spacing: 0.2px;
  }
  .brand-name { margin-right: 14px; padding-right: 14px; border-right: 1.5px solid rgba(255,255,255,0.6); }
  .notes {
    position: absolute; left: 90px; top: 78px; width: 690px;
    color: var(--white); font-size: 16px; line-height: 22px;
    list-style: none;
  }
  .notes li { padding-left: 20px; text-indent: -20px; margin-bottom: 5px; }
  .row {
    position: absolute; left: 17px; height: 40px;
    display: flex; align-items: center;
    color: var(--ink); font-size: 31px; white-space: nowrap;
  }
  .row--1 { top: 233px; } .row--2 { top: 291px; }
  .row--3 { top: 348px; } .row--4 { top: 405px; }
  .column--length .row { font-size: 25px; }
  .tick { width: 16px; height: 16px; margin-right: 22px; }
  .tick path { fill: none; stroke: var(--ink); stroke-width: 3; }
  .column-label {
    position: absolute; left: 54px; top: 503px; width: 169px; height: 53px;
    background: var(--button-red); border: 1.5px solid var(--button-edge);
    border-radius: 3px; box-shadow: 0 1px 2px rgba(0,0,0,0.25);
    color: var(--white); font-weight: 700; font-size: 25px;
    display: flex; align-items: center; justify-content: center;
  }
</style>
</head>
<body>
  <div class="chart-card">
    <div class="chart-panel">
      <div class="column column--size">
        <div class="row row--1"><svg class="tick" viewBox="0 0 16 16"><path d="M2 8.5 L6 12.5 L14 3"/></svg>Asian Size: S</div>
        <div class="row row--2"><svg class="tick" viewBox="0 0 16 16"><path d="M2 8.5 L6 12.5 L14 3"/></svg>Asian Size: M</div>
        <div class="row row--3"><svg class="tick" viewBox="0 0 16 16"><path d="M2 8.5 L6 12.5 L14 3"/></svg>Asian Size: L</div>
        <div class="row row--4"><svg class="tick" viewBox="0 0 16 16"><path d="M2 8.5 L6 12.5 L14 3"/></svg>Asian Size: XL</div>
        <div class="column-label">SIZE</div>
      </div>
      <div class="column column--bust">
        <div class="row row--1">Bust: 80cm/31,5″</div>
        <div class="row row--2">Bust: 84cm/33,1″</div>
        <div class="row row--3">Bust: 88cm/34,6″</div>
        <div class="row row--4">Bust: 92cm/36,2″</div>
        <div class="column-label">BUST</div>
      </div>
      <div class="column column--length">
        <div class="row row--1">Length: 80cm/31,5″</div>
        <div class="row row--2">Length: 82cm/32,3″</div>
        <div class="row row--3">Length: 84cm/33,1″</div>
        <div class="row row--4">Length: 86cm/33,9″</div>
        <div class="column-label">LENGTH</div>
      </div>

      <svg class="ribbon" viewBox="0 0 878 250">
        <defs>
          <linearGradient id="ribbonFill" x1="0" y1="0" x2="0" y2="1">
            <stop offset="0" stop-color="#e0504f"/>
            <stop offset="1" stop-color="#c94445"/>
          </linearGradient>
        </defs>
        <path d="M0 60 H878 V160 C720 196 580 240 439 242 C300 242 160 196 0 164 Z" fill="url(#ribbonFill)"/>
      </svg>

      <div class="chart-header"><span class="brand-name">TALVORO</span>SIZE DETAIL (1″=2,54CM)</div>

      <ol class="notes">
        <li>1.&nbsp; To make sure you get the right size, please refer to our size chart before buying. If you are not sure about size, please email us your exact body measurements, so we can give you some suggestions on how to choose the right size. Thanks for your understanding.</li>
        <li>2.&nbsp; Manual measurement may differ by 1-3cm</li>
      </ol>
    </div>
  </div>
</body>
</html>
```